Design needed for Cover of Conference Brochure

We are a conference company that puts on several business conferences per year. We are putting together a new conference - the Brightpath Insight Forum, and our audience is UX practitioners and specialists, product designers, UX designers, etc.
We need a brochure cover created. We are looking for fresh design ideas and are open to varying color schemes - please just keep in mind that this is a conference for business professionals, and fonts and colors should reflect this. Only restriction is that we do have a general cover format that we follow - i.e. which text goes where. (I've attached samples from our other events to reference.) We also generally have a central image to each brochure - feel free to submit a few versions with different images... we want something that accurately represents UX. However, if the design is compelling enough, image might not be completely necessary. We are relatively flexible - we just want something sharp!
- Must include KLVO logo (see placing on sample event covers)
- Must include footer - see sample covers
- Red text in word document are notes to you the designer - not actual text meant to appear on the cover
This cover is standard 8x11, and will be used for web only, not print. I have attached a word doc that includes all of the text that you will need for the cover. We will need final version in PDF, jpeg, and PSD. Please message me with any questions or clarification.

```html
<!DOCTYPE html>
<html lang="en">
<head>
<meta charset="utf-8">
<title>Brightpath Insight Forum — Brochure Cover</title>
<link rel="stylesheet" href="https://fonts.googleapis.com/css2?family=Bebas+Neue&family=Questrial&display=swap">
<style>
  :root {
    --teal: #1cc4b0;
    --teal-deep: #14a999;
    --dark: #2b2b2b;
    --dark-mid: #4a4a4a;
    --white: #ffffff;
    --skin: #e9b9a2;
  }
  * { margin: 0; padding: 0; box-sizing: border-box; }
  html, body { width: 873px; height: 1200px; overflow: hidden; background: var(--white); }
  .cover {
    position: relative; width: 873px; height: 1200px; overflow: hidden;
    font-family: "Questrial", "Helvetica Neue", sans-serif; color: var(--white);
  }
  .masthead {
    position: absolute; left: 0; top: 0; width: 873px; height: 256px;
    background: var(--teal); text-align: center;
  }
  .masthead__title {
    font-family: "Bebas Neue", "Oswald", sans-serif; font-weight: 400;
    font-size: 80px; letter-spacing: 1px; line-height: 1; padding-top: 52px;
  }
  .masthead__tagline { font-size: 36px; line-height: 42px; margin-top: 14px; }
  .stage {
    position: absolute; left: 0; top: 256px; width: 873px; height: 848px;
    background: radial-gradient(ellipse at 65% 45%, var(--dark-mid) 0%, var(--dark) 70%);
  }
  .stage__photo {
    position: absolute; left: 350px; top: 110px; width: 523px; height: 738px;
    background: radial-gradient(ellipse at 55% 55%, rgba(233,185,162,0.55) 0%, rgba(233,185,162,0.25) 40%, rgba(43,43,43,0) 72%);
  }
  .badge {
    position: absolute; border-radius: 50%; background: var(--teal);
    display: flex; flex-direction: column; align-items: center; justify-content: center; text-align: center;
  }
  .badge__label { font-family: "Bebas Neue", sans-serif; line-height: 1; }
  .badge--when { left: 195px; top: 48px; width: 178px; height: 178px; }
  .badge--when .badge__label { font-size: 52px; margin-bottom: 8px; }
  .badge--when .badge__text { font-size: 22px; line-height: 24px; }
  .badge--where { left: 32px; top: 206px; width: 238px; height: 238px; }
  .badge--where .badge__label { font-size: 52px; margin-bottom: 6px; }
  .badge--where .badge__text { font-size: 22px; line-height: 25px; }
  .early-bird {
    position: absolute; left: 644px; top: 50px;
    font-family: "Bebas Neue", sans-serif; font-size: 27px; line-height: 30px;
  }
  .highlights { position: absolute; left: 13px; top: 482px; width: 620px; }
  .highlights__item {
    height: 75px; margin-bottom: 17px; padding: 8px 0 0 14px;
    background: linear-gradient(90deg, rgba(28,196,176,0.85) 0%, rgba(28,196,176,0.6) 70%, rgba(28,196,176,0) 100%);
    font-size: 26px; line-height: 30px; text-shadow: 0 1px 2px rgba(0,0,0,0.35);
  }
  .brand {
    position: absolute; left: 726px; top: 790px; display: flex; align-items: center; gap: 8px;
  }
  .brand__mark { width: 24px; height: 24px; background: var(--teal); }
  .brand__name { font-size: 28px; color: var(--white); }
  .footer {
    position: absolute; left: 0; top: 1104px; width: 873px; height: 96px;
    background: var(--white); color: var(--teal-deep);
    display: flex; align-items: center; justify-content: space-between; padding: 0 22px 0 31px;
  }
  .footer__cta, .footer__phone { font-family: "Bebas Neue", sans-serif; font-size: 36px; }
  .footer__url { font-size: 24px; }
</style>
</head>
<body>
<div class="cover">
  <header class="masthead">
    <h1 class="masthead__title">BRIGHTPATH INSIGHT FORUM</h1>
    <p class="masthead__tagline">Design Compelling Experiences<br>through Successful UX Strategy</p>
  </header>

  <section class="stage">
    <div class="stage__photo" role="img" aria-label="Photo of a raised hand with faces drawn on the fingertips, paper cut-out business figures and floating social and web icons"></div>

    <div class="badge badge--when">
      <span class="badge__label">WHEN</span>
      <span class="badge__text">June 10-12<br>2014</span>
    </div>
    <div class="badge badge--where">
      <span class="badge__label">WHERE</span>
      <span class="badge__text">Harborview Club<br>&amp; Hotel<br>San Francisco, CA</span>
    </div>

    <p class="early-bird">REGISTER BY MARCH 7TH,<br>2014 AND SAVE $400!</p>

    <ul class="highlights" style="list-style:none">
      <li class="highlights__item">Design Compelling Experiences through<br>Successful UX Strategy</li>
      <li class="highlights__item">Learn How UX-Driven Innovation Can<br>Change Your Business</li>
      <li class="highlights__item">Build a Successful UX Team that Operates<br>Strategically</li>
      <li class="highlights__item">Insights into UX Research, User Behavior,<br>Usability Testing, Lean UX, and More</li>
    </ul>

    <div class="brand">
      <span class="brand__mark"></span>
      <span class="brand__name">KLVO</span>
    </div>
  </section>

  <footer class="footer">
    <span class="footer__cta">REGISTER TODAY!</span>
    <span class="footer__url">www.brightpathforum.com</span>
    <span class="footer__phone">888.555.0142</span>
  </footer>
</div>
</body>
</html>
```